'WILD' eye catching Business Card Design / Logo for production company / TV host / adventurer

Hi there,

We are looking for a 'WILD' and exciting logo and double sided business card for our business "Red Kettle Studios".

Corwin Baxley is an international television host, adventurer, author and inspirational public speaker.

We want to project Corwin's talents onto his business card.

We are looking for a business card design that can carry over onto letter heads, emails etc. We want a design that is 'WILD', different and exciting.

Feel free to check out Corwin's web site: www.redkettlestudios.co.nz to get a better understanding what he is about.

Please feel free to go completely 'WILD' on this project as we want something different with lots of WOW factors.

Thank you so much and we look forward to your designs.

We have a feeling that there will be many more designs in the near future.

Best regards,

the production team

We have added another task to the list.

If the winning designer can also provide us with a matching letterhead and email signature based on the same style of design as the business card.

Target Market(s)

People with passion.

Industry/Entity Type

Business

Requirements
Must have
• Red Kettle Studios
Corwin Baxley
42 Fernhill Lane
Ashbury 7388
New Zealand

Phone +64-(0)3-5027 416
Cell +64-(0)274-861 052

email: redkettlenz@mailbox-example.nz
www.redkettlestuios.co.nz
Nice to have
• A feature made out of the name 'Red Kettle Studios'.

Corwin Baxley's name reasonably obvious.

All other details (except web site) can be quite small.

```html
<!DOCTYPE html>
<html lang="en">
<head>
<meta charset="utf-8">
<title>Red Kettle Studios – Business Card</title>
<link rel="stylesheet" href="https://fonts.googleapis.com/css2?family=Anton&family=Arimo:wght@400;700&family=Noto+Sans:wght@600&display=swap">
<style>
  :root {
    --ink: #000000;
    --white: #ffffff;
    --name-from: #5fcf8a;
    --name-to: #a98fd8;
    --tagline: #4aa8e0;
    --cell: #ff1a1a;
    --address: #3fa0ff;
    --email: #ff4a2a;
    --web: #2ff0f0;
    --bg-yellow: #f6ff00;
    --bg-green: #27e81f;
    --bg-red: #ff1f1f;
    --bg-blue: #1e2fff;
    --bg-magenta: #ff2fd0;
    --bg-cyan: #1fe0ff;
    --bg-dark: #0a0a1a;
  }
  html, body {
    margin: 0;
    padding: 0;
    width: 1200px;
    height: 686px;
    overflow: hidden;
    background: var(--white);
  }
  .card {
    position: relative;
    width: 1200px;
    height: 686px;
    overflow: hidden;
    font-family: "Arimo", Arial, sans-serif;
  }
  .card__backdrop {
    position: absolute;
    inset: 0;
    background:
      radial-gradient(circle at 52% 40%, rgba(255,255,255,0.9) 0, rgba(255,255,255,0) 90px),
      radial-gradient(circle at 30% 48%, var(--bg-yellow) 0, rgba(246,255,0,0) 220px),
      radial-gradient(circle at 55% 8%, var(--bg-red) 0, rgba(255,31,31,0) 200px),
      radial-gradient(circle at 82% 25%, var(--bg-yellow) 0, rgba(246,255,0,0) 170px),
      radial-gradient(circle at 95% 70%, var(--bg-magenta) 0, rgba(255,47,208,0) 200px),
      radial-gradient(circle at 62% 68%, var(--bg-red) 0, rgba(255,31,31,0) 180px),
      radial-gradient(circle at 8% 22%, var(--bg-blue) 0, rgba(30,47,255,0) 220px),
      radial-gradient(circle at 18% 80%, var(--bg-cyan) 0, rgba(31,224,255,0) 170px),
      radial-gradient(circle at 40% 95%, var(--bg-magenta) 0, rgba(255,47,208,0) 180px),
      radial-gradient(circle at 75% 95%, var(--bg-blue) 0, rgba(30,47,255,0) 160px),
      linear-gradient(135deg, var(--bg-green) 0%, var(--bg-dark) 45%, var(--bg-green) 70%, var(--bg-dark) 100%);
  }
  .brand {
    position: absolute;
    left: 24px;
    top: 150px;
    margin: 0;
    font-family: "Anton", Impact, sans-serif;
    font-weight: 400;
    font-size: 72px;
    line-height: 1;
    color: var(--ink);
    letter-spacing: 1px;
  }
  .host {
    position: absolute;
    left: 736px;
    top: 190px;
    width: 464px;
  }
  .host__name {
    margin: 0;
    font-size: 64px;
    line-height: 1;
    font-weight: 400;
    background: linear-gradient(90deg, var(--name-from), var(--name-to));
    -webkit-background-clip: text;
    background-clip: text;
    color: transparent;
    white-space: nowrap;
  }
  .host__role {
    margin: 14px 0 0 18px;
    font-size: 24px;
    line-height: 1.3;
    font-weight: 700;
    color: var(--tagline);
    white-space: nowrap;
  }
  .host__role-line--light { color: var(--white); display: block; margin-left: 6px; }
  .host__cell {
    margin: 6px 0 0 4px;
    font-size: 33px;
    font-weight: 700;
    color: var(--cell);
    white-space: nowrap;
  }
  .contact {
    position: absolute;
    left: 94px;
    top: 440px;
    font-family: "Noto Sans", Verdana, sans-serif;
    font-weight: 600;
    font-size: 27px;
    line-height: 35px;
  }
  .contact__line { margin: 0; white-space: nowrap; }
  .contact__line--street, .contact__line--town { color: var(--address); }
  .contact__line--country, .contact__line--phone { color: var(--white); }
  .contact__line--email { color: var(--email); font-size: 25px; }
  .website {
    position: absolute;
    left: 92px;
    top: 622px;
    margin: 0;
    font-family: "Arimo", Arial, sans-serif;
    font-size: 42px;
    font-weight: 400;
    color: var(--web);
    white-space: nowrap;
  }
</style>
</head>
<body>
  <main class="card">
    <div class="card__backdrop" role="img" aria-label="Vivid abstract backdrop of blended yellow, green, red, blue and magenta colour fields"></div>

    <h1 class="brand">RED KETTLE STUDIOS</h1>

    <section class="host">
      <h2 class="host__name">Corwin Baxley</h2>
      <p class="host__role">Television host,adventurer ,author
        <span class="host__role-line--light">and inspiratinal public speaker</span>
      </p>
      <p class="host__cell">cell:64-(0)274-861 052</p>
    </section>

    <address class="contact">
      <p class="contact__line contact__line--street">42 Fernhill Lane</p>
      <p class="contact__line contact__line--town">Ashbury 7388</p>
      <p class="contact__line contact__line--country">New Zealand</p>
      <p class="contact__line contact__line--phone">Phone:64-(0)3-5027 416</p>
      <p class="contact__line contact__line--email">email:redkettlenz@mailbox-example.nz</p>
    </address>

    <p class="website">www.redkettlestudios.co.nz</p>
  </main>
</body>
</html>
```